Business Card Design

We would like a business card that utilizes our current logo and keeps with the same feel - elegant and organic. Our farm isn't about mass production, it's about excellence, education, beautiful events and flowers - people, culture, and community.

Target Market(s)

Patrons to our farm who are interested in weddings, events, or our flowers and vegetables.

Contact Information for Business Card

Name, address, cell email (Danielle Hoskins, 2716 Wrenfield Rd, Alderbrook, CO 80517, cell 30.412.6638, email danielle@wrenfieldacres.com)

```html
<!DOCTYPE html>
<html lang="en">
<head>
<meta charset="utf-8">
<title>Wrenfield Acres — Business Card</title>
<link rel="stylesheet" href="https://fonts.googleapis.com/css2?family=Open+Sans:wght@400;600&family=Pinyon+Script&display=swap">
<style>
  :root {
    --backdrop: #e9e6e1;
    --bark: #4f3b24;
    --sage: #728c7d;
    --sage-deep: #5e786a;
    --sage-pale: #8fa99a;
    --paper: #ffffff;
    --paper-shade: #eeeeee;
    --tan: #c4a486;
    --ink: #3f4a44;
  }
  * { box-sizing: border-box; margin: 0; padding: 0; }
  html, body { width: 1200px; height: 900px; overflow: hidden; }
  body {
    background: var(--backdrop);
    font-family: "Open Sans", sans-serif;
    position: relative;
  }
  .card {
    position: absolute;
    left: 320px;
    width: 560px;
    height: 320px;
    overflow: hidden;
    box-shadow: 0 10px 28px rgba(0,0,0,0.18);
  }
  .card--front {
    top: 90px;
    background: var(--bark);
    border-radius: 34px 6px 34px 6px;
  }
  .card--back {
    top: 490px;
    background: linear-gradient(100deg, var(--paper) 0%, var(--paper-shade) 45%, var(--paper) 75%);
    border-radius: 6px 34px 6px 34px;
  }
  .band { position: absolute; inset: 0; width: 100%; height: 100%; }
  .leaf-art {
    position: absolute;
    background: var(--sage-deep);
    border-radius: 22px;
  }
  .card--front .leaf-art { left: 34px; top: 36px; width: 130px; height: 220px; }
  .card--back .leaf-art { left: 425px; top: 26px; width: 105px; height: 190px; }

  .wordmark {
    position: absolute;
    font-family: "Open Sans", sans-serif;
    font-weight: 400;
    letter-spacing: 0.22em;
    text-transform: uppercase;
    color: var(--sage-pale);
    display: flex;
    align-items: center;
    gap: 12px;
  }
  .wordmark__dot {
    width: 10px; height: 10px; border-radius: 50%;
    background: currentColor; flex: none;
  }
  .card--front .wordmark { left: 250px; top: 146px; font-size: 22px; }
  .card--back .wordmark { left: 36px; top: 50px; font-size: 20px; color: var(--sage-deep); }

  .contact {
    position: absolute;
    left: 36px;
    top: 145px;
    width: 340px;
    color: var(--ink);
  }
  .contact__name {
    font-family: "Pinyon Script", cursive;
    font-size: 32px;
    color: var(--sage-deep);
    line-height: 1.1;
    margin-bottom: 10px;
  }
  .rule { height: 1px; background: var(--tan); margin: 8px 0 8px; }
  .contact__row {
    display: flex; align-items: center; gap: 9px;
    font-size: 13px; line-height: 22px;
  }
  .contact__row svg { width: 13px; height: 13px; flex: none; fill: var(--sage-deep); }
</style>
</head>
<body>

<section class="card card--front" aria-label="Business card front">
  <svg class="band" viewBox="0 0 560 320" preserveAspectRatio="none" aria-hidden="true">
    <path d="M0,0 L150,0 C128,110 140,230 196,320 L0,320 Z" fill="var(--sage)"/>
  </svg>
  <div class="leaf-art" role="img" aria-label="Illustration of a sage green leafy sprig"></div>
  <div class="wordmark"><span class="wordmark__dot"></span>Wrenfield Acres</div>
</section>

<section class="card card--back" aria-label="Business card back">
  <svg class="band" viewBox="0 0 560 320" preserveAspectRatio="none" aria-hidden="true">
    <path d="M395,0 L560,0 L560,300 C495,270 455,190 395,0 Z" fill="var(--sage)"/>
  </svg>
  <div class="leaf-art" role="img" aria-label="Illustration of a sage green leafy sprig"></div>
  <div class="wordmark"><span class="wordmark__dot"></span>Wrenfield Acres</div>

  <div class="contact">
    <p class="contact__name">Danielle Hoskins</p>
    <p class="contact__row">
      <svg viewBox="0 0 16 16" aria-hidden="true"><path d="M4 1h8a1 1 0 0 1 1 1v12a1 1 0 0 1-1 1H4a1 1 0 0 1-1-1V2a1 1 0 0 1 1-1zm0.6 1.6v9.8h6.8V2.6zM8 13a.7.7 0 1 0 0 .01z"/></svg>
      30.412.6638
    </p>
    <p class="contact__row">
      <svg viewBox="0 0 16 16" aria-hidden="true"><path d="M1 3h14v10H1zm1.4 1.3L8 8.6l5.6-4.3zM2.3 5.6v6.1h11.4V5.6L8 10z"/></svg>
      danielle@wrenfieldacres.com
    </p>
    <div class="rule"></div>
    <p class="contact__row">
      <svg viewBox="0 0 16 16" aria-hidden="true"><path d="M8 0a5.5 5.5 0 0 1 5.5 5.5C13.5 10 8 16 8 16S2.5 10 2.5 5.5A5.5 5.5 0 0 1 8 0zm0 3.3a2.2 2.2 0 1 0 0 4.4 2.2 2.2 0 0 0 0-4.4z"/></svg>
      2716 Wrenfield Rd, Alderbrook, CO 80517
    </p>
  </div>
</section>

</body>
</html>
```